signboard Marvolek

Hi, We are a language school and we register students abroad in Germany. We-have a lot of department and we need a signboard For Each department so students can Distinguish Each department. The design is the Sámi for all the departments. Only texts changes. List of departments: - Visa - Pre-university enrollment - Translations - Language school - Sales We need a Design that respect our logo colors, with our logo Thank u Waiting for proposals

School

```html
<!DOCTYPE html>
<html lang="fr">
<head>
<meta charset="UTF-8">
<title>Marvolek – Signalétique</title>
<link rel="stylesheet" href="https://fonts.googleapis.com/css2?family=Oswald:wght@500;600&display=swap">
<style>
  :root {
    --wall: #d9dde3;
    --panel-top: #5c5c5c;
    --panel-bottom: #0e0e0e;
    --accent: #e3e024;
    --ink: #1b1b1b;
    --white: #ffffff;
  }
  html, body {
    margin: 0;
    padding: 0;
    width: 1200px;
    height: 900px;
    overflow: hidden;
    background: var(--wall);
  }
  .signboard {
    position: absolute;
    left: 100px;
    top: 170px;
    width: 1000px;
    height: 560px;
    overflow: hidden;
    background: linear-gradient(180deg, var(--panel-top) 0%, #2b2b2b 55%, var(--panel-bottom) 100%);
    font-family: "Oswald", "Arial Narrow", sans-serif;
  }
  .signboard__band {
    position: absolute;
    inset: 0;
    width: 1000px;
    height: 560px;
  }
  .brand {
    position: absolute;
    left: 58px;
    top: 78px;
    display: flex;
    align-items: center;
    gap: 16px;
  }
  .brand__dot {
    width: 34px;
    height: 34px;
    border-radius: 50%;
    background: var(--accent);
  }
  .brand__name {
    color: var(--white);
    font-weight: 600;
    font-size: 66px;
    line-height: 1;
    letter-spacing: -0.5px;
  }
  .department {
    position: absolute;
    right: 24px;
    top: 318px;
    margin: 0;
    text-align: right;
    color: var(--ink);
    font-weight: 600;
    font-size: 58px;
    line-height: 92px;
    letter-spacing: -0.5px;
    text-transform: uppercase;
  }
</style>
</head>
<body>
  <div class="signboard">
    <svg class="signboard__band" viewBox="0 0 1000 560" aria-hidden="true">
      <rect class="band__outline" x="381" y="236" width="800" height="370" rx="185" fill="none" stroke="#e3e024" stroke-width="22"/>
      <rect class="band__fill" x="426" y="272" width="800" height="290" rx="145" fill="#e3e024"/>
    </svg>
    <div class="brand">
      <span class="brand__name">Marvolek</span>
      <span class="brand__dot"></span>
    </div>
    <h1 class="department">Pré-inscriptions<br>universitaires</h1>
  </div>
</body>
</html>
```